Geschäftspapier-Design für Anbieter einer Online-Ausbildung für den qualifizierten Krankentransport und Rettungsdienst
Zielgruppe
LOTH Online-Ausbildung für den qualifizierten Krankentransport und Rettungsdienst
Der qualifizierte Krankentransport und Rettungsdienst ist zuständig für den Transport- und die Versorgung von kranken und verletzten Menschen. LOTH Medizinische Ausbildung und Seminare hat sich als Privatschule für die präklinische Notfallmedizin auf Aus- und Weiterbildungen im E-Learning-Modul für diese zwei Fachbereiche spezialisiert. Alle unsere Fachausbildungen sind online in unserem modernen Campus mit überregionalem Zugang absolvierbar.
Aufgabenstellung
Wir benötigen eine Word-Briefvorlage für den alltäglichen Geschäftsverkehr in drei Ausführungen.
- Briefvorlage mit Angabe der Abteilung -> Sekretariat
- Briefvorlage mit Angabe der Abteilung -> Schulleitung
- Briefvorlage mit Angabe der Abteilung -> Geschäftsführung
- Briefvorlage mit Angabe der Abteilung -> Buchhaltung/ Forderungsmanagement
Die Vorlage sollte bitte folgende Angaben aufweisen:
LOTH Bildungsgesellschaft UG (haftungsbeschränkt)
Privatschule für prähospitale Rettungsmedizin
Standort unserer Verwaltung:
Farnhügel 7
15537 Erkner
Standort unseres Schulsitzes:
Am Quendelhof 48
D- 15537 Gosen- Neu Zittau
Schulleitung: Jutta Wildgrube & Matthias Lot
Ärztliche Leitung: Dr. Med. Ortwin Brasch
Pädagogische Leitung: Matthias Loth
Fachlicher Beirat: Dr. rer. med. Fabian Oswalt
Tel: 030 6270384 50
Fax: 030 6270384 51
E-Mail: info@loth-lehrwerkstatt.de
Web: www.loth-lehrwerkstatt.de
Vertreten durch: Jutta Wildgrube
Registereintrag: Eintragung im Handelsregister Registergericht: Amtsgericht Frankfurt (Oder) Registernummer: HRB 27403 FF

```html
<!DOCTYPE html>
<html lang="de">
<head>
<meta charset="utf-8">
<title>LOTH Bildungsgesellschaft – Briefbogen Sekretariat</title>
<link rel="stylesheet" href="https://fonts.googleapis.com/css2?family=Source+Sans+3:wght@400;600;700&display=swap">
<style>
  :root {
    --brand-blue: #6fa8d8;
    --ink: #1a171b;
    --paper: #ffffff;
  }
  * { margin: 0; padding: 0; box-sizing: border-box; }
  html, body { width: 862px; height: 1200px; overflow: hidden; background: var(--paper); }
  body { font-family: "Source Sans 3", sans-serif; color: var(--ink); }
  .letterhead { position: relative; width: 862px; height: 1200px; }
  .page-frame {
    position: absolute; left: 38px; top: 43px; width: 786px; height: 1114px;
    border: 1px solid var(--ink);
  }
  .bands { position: absolute; left: 0; top: 0; }
  .brand-mark {
    position: absolute; left: 462px; top: 132px;
    display: flex; align-items: center; gap: 6px;
    font-size: 22px; font-weight: 700; color: var(--brand-blue); letter-spacing: 0.5px;
  }
  .brand-mark .square { width: 14px; height: 14px; background: var(--brand-blue); }
  .brand-divider {
    position: absolute; left: 559px; top: 92px; width: 1px; height: 111px; background: var(--ink);
  }
  .company {
    position: absolute; left: 578px; top: 116px;
    font-size: 12.2px; font-weight: 600; line-height: 16px;
  }
  .company .tagline { margin-top: 4px; }
  .sender-line {
    position: absolute; left: 139px; top: 220px;
    font-size: 9.2px; padding-bottom: 1px; border-bottom: 1px solid var(--ink); width: 262px;
  }
  .address-mark { position: absolute; top: 387px; width: 1.5px; height: 1.5px; background: var(--ink); }
  .fold-mark { position: absolute; left: 38px; width: 14px; height: 1px; background: var(--ink); }
  .department {
    position: absolute; left: 578px; top: 214px;
    font-size: 13.4px; font-weight: 700; color: var(--brand-blue);
  }
  .contact { position: absolute; left: 578px; top: 236px; font-size: 10.4px; line-height: 14px; }
  .contact .label { color: var(--brand-blue); }
  .contact .group { margin-bottom: 3.5px; }
  .footer-col { position: absolute; top: 1087px; font-size: 8.4px; line-height: 11.3px; }
  .footer-col .label { color: var(--brand-blue); font-weight: 600; }
</style>
</head>
<body>
<div class="letterhead">
  <div class="page-frame"></div>

  <svg class="bands" width="862" height="1200" aria-hidden="true">
    <polygon points="38,43 555,43 542,58 38,58" fill="var(--brand-blue)"/>
    <polygon points="593,43 824,43 824,58 579,58" fill="var(--ink)"/>
    <polygon points="38,1141 567,1141 552,1157 38,1157" fill="var(--ink)"/>
    <polygon points="600,1141 824,1141 824,1157 585,1157" fill="var(--brand-blue)"/>
  </svg>

  <div class="brand-mark"><span class="square"></span>LOTH</div>
  <div class="brand-divider"></div>

  <div class="company">
    <p>LOTH Bildungsgesellschaft UG<br>(haftungsbeschränkt)</p>
    <p class="tagline">Privatschule für<br>prähospitale Rettungsmedizin</p>
  </div>

  <p class="sender-line">LOTH Bildungsgesellschaft UG&nbsp; | &nbsp;Farnhügel 7&nbsp; | &nbsp;15537 Erkner</p>

  <span class="address-mark" style="left:112px"></span>
  <span class="address-mark" style="left:430px"></span>
  <span class="fold-mark" style="top:436px"></span>
  <span class="fold-mark" style="top:599px"></span>

  <p class="department">– Sekretariat –</p>

  <div class="contact">
    <div class="group"><span class="label">Verwaltung:</span><br>Farnhügel 7<br>15537 Erkner</div>
    <div class="group"><span class="label">Schulsitz:</span><br>Am Quendelhof 48<br>15537 Gosen-Neu Zittau</div>
    <div class="group">Tel. 030&nbsp; 6270384 50<br>Fax 030&nbsp; 6270384 51</div>
    <div class="group">E-Mail: info@loth-lehrwerkstatt.de<br>Web: www.loth-lehrwerkstatt.de</div>
  </div>

  <div class="footer-col" style="left:75px">
    <span class="label">Schulleitung:</span> Jutta Wildgrube · Matthias Loth<br>
    <span class="label">Ärztliche Leitung:</span> Dr. med. Ortwin Brasch<br>
    <span class="label">Pädagogische Leitung:</span> Matthias Loth<br>
    <span class="label">Fachlicher Beirat:</span> Dr. rer. med. Fabian Oswalt
  </div>
  <div class="footer-col" style="left:345px">
    <span class="label">Vertreten durch:</span> Jutta Wildgrube<br>
    <span class="label">Registereintrag:</span> Eintragung im Handelsregister<br>
    <span class="label">Registergericht:</span> Amtsgericht Frankfurt (Oder)<br>
    <span class="label">Registernummer:</span> HRB 27403 FF
  </div>
  <div class="footer-col" style="left:610px">
    <span class="label">Kontoverbindung:</span><br>
    Spreeufer Bank<br>
    IBAN: DE00 0000 0000 0000 0000 00<br>
    BIC: XXXXXXXXXXX
  </div>
</div>
</body>
</html>
```